Building company buisness cards

We are looking for a sharp modern new look for our business cards.
We are a New Zealand based company that specialises in house and land packages.
We have attached a photo of the current logo and would like to see if it can be improved somehow if needed.
We are open to any colours but we have chosen green at this stage.
Feel free to change the font and make the logo smarter looking.
Play with the colours and see what looks best.

We want a card that looks so good know one will want to throw it away!

Target Market(s)

Home buyers

Industry/Entity Type

Building

Contact Information for Business Card

Dorian Keswick
0217392604
dkeswick@tidewellhomecraft.co.nz
tidewellhomecraft.co.nz

Font styles to use
Serif
Sans Serif

Colors

Designer to choose colors to be used in the design.

Requirements
Must have
• Logo and company name on one side, details on the other side
Nice to have
• Color codes for the original green are HEX #4a8028, RGB(74,128,40), CMYK(42,0,69,50)
• Round corners, Raised and/or spot UV

```html
<!DOCTYPE html>
<html lang="en">
<head>
<meta charset="utf-8">
<title>Tidewell Homecraft – Business Cards</title>
<link href="https://fonts.googleapis.com/css2?family=Montserrat:wght@400;500;700;800&display=swap" rel="stylesheet">
<style>
  :root {
    --brand-green: #4a8028;
    --deep-green: #3f7a2a;
    --ink: #2b2b2b;
    --paper: #ffffff;
    --stone: #a3a3a3;
    --backdrop: #e6e6e4;
  }
  * { box-sizing: border-box; margin: 0; padding: 0; }
  html, body {
    width: 1200px; height: 780px; overflow: hidden;
    background: var(--backdrop);
    font-family: "Montserrat", sans-serif;
  }
  .canvas {
    position: relative; width: 1200px; height: 780px;
  }
  .card {
    position: absolute; top: 240px;
    width: 520px; height: 300px;
    border-radius: 10px; overflow: hidden;
    box-shadow: 0 6px 18px rgba(0,0,0,0.15);
  }
  /* Front side */
  .card-front {
    left: 50px; background: var(--brand-green); color: var(--paper);
    display: flex; flex-direction: column; align-items: center; justify-content: center;
  }
  .brand-mark {
    display: flex; align-items: center; gap: 12px;
  }
  .brand-dot {
    width: 16px; height: 16px; border-radius: 50%; background: currentColor;
  }
  .brand-name {
    font-weight: 800; font-size: 40px; letter-spacing: -0.5px; line-height: 1;
  }
  .front-url {
    margin-top: 34px; font-size: 14px; font-weight: 400; letter-spacing: 0.3px;
  }
  /* Back side */
  .card-back { left: 630px; background: var(--paper); color: var(--ink); }
  .card-back .brand-mark {
    position: absolute; top: 58px; right: 34px; color: var(--deep-green);
  }
  .card-back .brand-name { font-size: 30px; }
  .card-back .brand-dot { width: 12px; height: 12px; }
  .rule {
    position: absolute; height: 2px; background: var(--deep-green);
  }
  .rule-top { top: 126px; left: 90px; right: 34px; }
  .rule-mid { top: 190px; left: 34px; right: 100px; }
  .holder {
    position: absolute; top: 140px; left: 34px;
  }
  .holder-name {
    color: var(--deep-green); font-weight: 700; font-size: 20px; line-height: 1.1;
  }
  .holder-role { font-size: 15px; font-weight: 500; margin-top: 2px; }
  .contact-list {
    position: absolute; top: 204px; left: 34px; list-style: none;
    font-size: 15px; line-height: 21px;
  }
  .contact-list li { display: flex; align-items: center; gap: 8px; }
  .contact-list svg { width: 11px; height: 11px; fill: none; stroke: var(--deep-green); stroke-width: 2; flex: none; }
  .base-bands { position: absolute; left: 0; bottom: 0; width: 520px; height: 40px; }
</style>
</head>
<body>
<main class="canvas">
  <section class="card card-front" aria-label="Card front">
    <div class="brand-mark">
      <span class="brand-dot"></span>
      <span class="brand-name">Tidewell Homecraft</span>
    </div>
    <p class="front-url">tidewellhomecraft.co.nz</p>
  </section>

  <section class="card card-back" aria-label="Card back">
    <div class="brand-mark">
      <span class="brand-dot"></span>
      <span class="brand-name">Tidewell Homecraft</span>
    </div>
    <div class="rule rule-top"></div>
    <div class="holder">
      <p class="holder-name">Dorian Keswick</p>
      <p class="holder-role">Founder</p>
    </div>
    <div class="rule rule-mid"></div>
    <ul class="contact-list">
      <li><svg viewBox="0 0 12 12"><path d="M2 1.5l2 0 1 2.5-1.3 1a6 6 0 0 0 3.3 3.3l1-1.3 2.5 1 0 2c-5 .5-9-3.5-8.5-8.5z"/></svg>0217392604</li>
      <li><svg viewBox="0 0 12 12"><rect x="1" y="2.5" width="10" height="7"/><path d="M1 2.5l5 4 5-4"/></svg>dkeswick@tidewellhomecraft.co.nz</li>
      <li><svg viewBox="0 0 12 12"><circle cx="6" cy="6" r="5"/><path d="M1 6h10M6 1c-3 3-3 7 0 10M6 1c3 3 3 7 0 10"/></svg>tidewellhomecraft.co.nz</li>
    </ul>
    <svg class="base-bands" viewBox="0 0 520 40" preserveAspectRatio="none" aria-hidden="true">
      <polygon points="0,30 330,30 330,40 0,40" fill="var(--deep-green)"/>
      <polygon points="338,40 350,18 520,8 520,40" fill="var(--stone)"/>
    </svg>
  </section>
</main>
</body>
</html>
```